Courtside Heritage Trust Web site

We need a Wordpress web site for a new non-profit, the Courtside Heritage Trust. CHT's mission is to raise the awareness of sustainability within the tennis community and industry worldwide. Our focus is on education and being a catalyst in connecting expertise in the environmental field with tennis organizations to create sustainable change. Our primary targets are youth education and empowerment, tennis facility management, and Celebrity tennis players' engagement.

The design needs to be elegant and attractive to potential corporate donors and reflect the high level of sophistication of the tennis demographic. It needs to be very graphic with high-impact photos and the ability to inspire action. Although it can be simple now it will need to have the capability of expanding to allow acceptance of donations online, offering of information products in exchange for email registration, and potentially a membership-oriented section of the site with forums and community engagement.

At the present time, it is more of an information-oriented site that tells a compelling story and inspires people to take action to get involved in the way that most fits their needs.

We need to have the ability to add pages and blog posts easily on our own while maintaining a relationship that would allow us a cost-effective way of making more major additions and adjustments to the site.

Attached is our logo. Thanks for your desire to help us make an impact on the world.

Industry/Entity Type

Graphic Design

```html
<!DOCTYPE html>
<html lang="en">
<head>
<meta charset="utf-8">
<title>Courtside Heritage Trust — Blog</title>
<link rel="stylesheet" href="https://fonts.googleapis.com/css2?family=Open+Sans:ital,wght@0,300;0,400;0,600;0,700;1,400&display=swap">
<style>
  :root {
    --teal: #0e6583;
    --teal-dark: #0b5570;
    --yellow: #d8c600;
    --olive-1: #a6a45a;
    --olive-2: #c7c684;
    --olive-3: #8b8a45;
    --page: #f2f2f2;
    --white: #ffffff;
    --text: #8a8a8a;
    --text-dark: #3e3e3e;
    --line: #d9d9d9;
    --field: #e4e4e4;
    --footer: #363d45;
    --footer-text: #9aa1a8;
    --icon-grey: #7d8288;
  }
  * { box-sizing: border-box; margin: 0; padding: 0; }
  html, body { width: 876px; height: 1200px; overflow: hidden; }
  body {
    position: relative;
    background: var(--page);
    font-family: "Open Sans", Arial, sans-serif;
    color: var(--text);
  }
  ul { list-style: none; }

  /* Header */
  .site-header {
    position: absolute; left: 0; top: 0; width: 876px; height: 160px;
  }
  .header-photo {
    position: absolute; inset: 0;
    background:
      radial-gradient(ellipse 150px 150px at 110px 60px, var(--olive-2), transparent 70%),
      radial-gradient(ellipse 260px 120px at 720px 140px, var(--olive-3), transparent 75%),
      linear-gradient(100deg, var(--olive-2) 0%, var(--olive-1) 40%, var(--olive-3) 100%);
  }
  .brand {
    position: absolute; left: 171px; top: 54px;
    font-size: 11px; font-weight: 600; letter-spacing: .2px;
    color: var(--teal);
    text-transform: uppercase;
  }
  .become-member {
    position: absolute; right: 168px; top: 57px;
    display: flex; align-items: center; gap: 5px;
    font-size: 8.5px; font-weight: 600; color: var(--white);
  }
  .become-member .mark { width: 9px; height: 9px; background: var(--teal); }
  .main-nav {
    position: absolute; left: 172px; top: 79px; width: 536px; height: 37px;
    display: flex; background: var(--white);
  }
  .main-nav a {
    flex: 1; display: flex; align-items: center; justify-content: center;
    font-size: 8.5px; color: var(--text-dark); text-decoration: none;
    border-right: 1px solid #e6e6e6;
  }
  .main-nav a:last-child { border-right: 0; }
  .main-nav a.active { background: var(--teal); color: var(--white); }

  /* Blog column */
  .page-title {
    position: absolute; left: 172px; top: 190px;
    font-size: 23px; font-weight: 300; color: var(--teal);
  }
  .post { position: absolute; left: 172px; width: 365px; height: 170px; }
  .post-date {
    position: absolute; left: 0; top: 0; width: 36px; height: 40px;
  }
  .post-date .day {
    position: absolute; left: 0; top: 14px; width: 36px; text-align: center;
    font-size: 11px; font-weight: 700; color: var(--teal);
  }
  .post-date .month {
    position: absolute; left: 0; top: 28px; width: 36px; text-align: center;
    font-size: 4.5px; font-weight: 700; color: var(--teal); text-transform: uppercase;
  }
  .post-title {
    position: absolute; left: 53px; top: -2px;
    font-size: 10px; font-weight: 400; color: var(--yellow); text-transform: uppercase;
  }
  .post-meta {
    position: absolute; left: 53px; top: 13px; width: 312px;
    display: flex; justify-content: space-between;
    font-size: 6.5px; color: var(--text);
  }
  .post-meta .comments { font-style: italic; }
  .post-image {
    position: absolute; left: 0; top: 45px; width: 148px; height: 122px;
  }
  .post-excerpt {
    position: absolute; left: 161px; top: 42px; width: 204px;
    font-size: 7px; font-weight: 600; line-height: 12px; color: #9a9a9a;
    text-align: justify;
  }
  .post-excerpt p + p { margin-top: 12px; }
  .read-more {
    position: absolute; right: 0; top: 148px; width: 59px; height: 19px;
    border: 1px solid var(--text-dark);
    display: flex; align-items: center; justify-content: center;
    font-size: 6.5px; font-weight: 600; color: var(--text-dark); text-transform: uppercase;
  }
  .photo-court { background: linear-gradient(90deg, #8a3a2c 0%, #a0483a 45%, #1d4fa2 55%, #1a4496 100%); }
  .photo-player { background: linear-gradient(160deg, #4e4b44 0%, #6b6254 50%, #9b7fb2 100%); }
  .photo-group { background: linear-gradient(180deg, #5b7a3d 0%, #8c6a63 50%, #3b3b3f 100%); }
  .photo-match { background: linear-gradient(180deg, #2c2a2e 0%, #5c4a55 45%, #c2456a 70%, #4c5a4a 100%); }

  .pagination {
    position: absolute; left: 172px; top: 1027px; display: flex; gap: 3px;
  }
  .pagination span {
    width: 18px; height: 18px; border: 1px solid #c9c9c9;
    display: flex; align-items: center; justify-content: center;
    font-size: 7px; color: var(--text);
  }
  .pagination span.current { border-color: var(--yellow); color: var(--text-dark); }

  /* Sidebar */
  .sidebar { position: absolute; left: 555px; top: 197px; width: 153px; }
  .search { display: flex; height: 22px; }
  .search .button {
    width: 26px; background: var(--teal);
    display: flex; align-items: center; justify-content: center;
  }
  .search .field {
    flex: 1; background: var(--field); padding-left: 8px;
    display: flex; align-items: center;
    font-size: 7px; color: var(--white);
  }
  .widget-title {
    position: absolute; left: 0;
    font-size: 16px; font-weight: 300; color: var(--teal); text-transform: uppercase;
  }
  .link-list { position: absolute; left: 0; }
  .link-list li {
    height: 16px; display: flex; align-items: center; gap: 7px;
    font-size: 7px; color: var(--teal-dark); text-transform: uppercase;
  }
  .comment-list { position: absolute; left: 0; top: 464px; width: 153px; }
  .comment-list li { display: flex; height: 33px; }
  .comment-list .avatar {
    width: 22px; height: 22px; background: #dcdcdc; flex: none;
  }
  .comment-list .body { margin-left: 8px; flex: 1; }
  .comment-list .author { font-size: 6.5px; font-weight: 700; color: var(--teal); }
  .comment-list .author em { font-style: normal; font-weight: 400; color: var(--text); }
  .comment-list .quote {
    margin-top: 1px; height: 12px; background: var(--white);
    font-size: 4.5px; font-style: italic; color: var(--text);
    padding-left: 3px; display: flex; align-items: center;
  }

  /* Footer */
  .site-footer {
    position: absolute; left: 0; top: 1124px; width: 876px; height: 76px;
    background: var(--footer);
  }
  .footer-block {
    position: absolute; top: 30px;
    font-size: 7.5px; line-height: 8.5px; color: var(--footer-text); text-transform: uppercase;
  }
  .footer-icon { position: absolute; top: 32px; }
  .footer-legal {
    position: absolute; left: 541px; top: 30px; width: 170px;
    font-size: 6.8px; color: var(--footer-text); white-space: nowrap;
  }
  .footer-legal .name { color: var(--yellow); text-transform: uppercase; }
  .social { position: absolute; left: 541px; top: 43px; display: flex; gap: 3px; }
  .social span { width: 18px; height: 18px; border-radius: 50%; background: var(--icon-grey); }
</style>
</head>
<body>

<header class="site-header">
  <div class="header-photo" role="img" aria-label="Close-up of a tennis ball against a court net, tinted olive"></div>
  <div class="brand">Courtside Heritage Trust</div>
  <div class="become-member"><span class="mark"></span>BECOME A MEMBER</div>
  <nav class="main-nav">
    <a href="#">HOME</a>
    <a href="#">EVENTS</a>
    <a href="#">MEMBERS</a>
    <a href="#" class="active">BLOG</a>
    <a href="#">CONTACT</a>
  </nav>
</header>

<main>
  <h1 class="page-title">OUR BLOG</h1>

  <article class="post" style="top:230px">
    <div class="post-date">
      <svg width="36" height="40" viewBox="0 0 36 40"><rect x="1" y="5" width="34" height="34" rx="3" fill="#fff" stroke="#cfcfcf" stroke-width="2"/><rect x="1" y="5" width="34" height="8" fill="#d4d4d4"/><rect x="8" y="1" width="3" height="8" rx="1" fill="#bdbdbd"/><rect x="25" y="1" width="3" height="8" rx="1" fill="#bdbdbd"/></svg>
      <span class="day">15</span><span class="month">March</span>
    </div>
    <h2 class="post-title">Lorem ipsum dolor sit amet consectetuer</h2>
    <div class="post-meta"><span>Posted by Admin</span><span class="comments">5 Comments</span></div>
    <div class="post-image photo-court" role="img" aria-label="Player serving on a red and blue hard court"></div>
    <div class="post-excerpt">
      <p>Lorem ipsum dolor sit amet, consectetur adipiscing elit. Sed lacus mi, sollicitudin vehicula sapien ac, sodales eleifend nisl. Aenean vestibulum justo ac ultrices facilisis. Aliquam sit amet fringilla justo. Phasellus at suscipit mauris.</p>
      <p>Morbi eget diam nisi. Pellentesque dapibus faucibus neque. Cras pulvinar semper orci adipiscing commodo. Mauris ullamcorper arcu vel rutrum ultricies.</p>
    </div>
    <a class="read-more">Read more</a>
  </article>

  <article class="post" style="top:432px">
    <div class="post-date">
      <svg width="36" height="40" viewBox="0 0 36 40"><rect x="1" y="5" width="34" height="34" rx="3" fill="#fff" stroke="#cfcfcf" stroke-width="2"/><rect x="1" y="5" width="34" height="8" fill="#d4d4d4"/><rect x="8" y="1" width="3" height="8" rx="1" fill="#bdbdbd"/><rect x="25" y="1" width="3" height="8" rx="1" fill="#bdbdbd"/></svg>
      <span class="day">17</span><span class="month">September</span>
    </div>
    <h2 class="post-title">Lorem ipsum dolor sit amet consectetuer</h2>
    <div class="post-meta"><span>Posted by Admin</span><span class="comments">5 Comments</span></div>
    <div class="post-image photo-player" role="img" aria-label="Smiling player in a lilac top holding a racket"></div>
    <div class="post-excerpt">
      <p>Lorem ipsum dolor sit amet, consectetur adipiscing elit. Sed lacus mi, sollicitudin vehicula sapien ac, sodales eleifend nisl. Aenean vestibulum justo ac ultrices facilisis. Aliquam sit amet fringilla justo. Phasellus at suscipit mauris.</p>
      <p>Morbi eget diam nisi. Pellentesque dapibus faucibus neque. Cras pulvinar semper orci adipiscing commodo. Mauris ullamcorper arcu vel rutrum ultricies.</p>
    </div>
    <a class="read-more">Read more</a>
  </article>

  <article class="post" style="top:634px">
    <div class="post-date">
      <svg width="36" height="40" viewBox="0 0 36 40"><rect x="1" y="5" width="34" height="34" rx="3" fill="#fff" stroke="#cfcfcf" stroke-width="2"/><rect x="1" y="5" width="34" height="8" fill="#d4d4d4"/><rect x="8" y="1" width="3" height="8" rx="1" fill="#bdbdbd"/><rect x="25" y="1" width="3" height="8" rx="1" fill="#bdbdbd"/></svg>
      <span class="day">19</span><span class="month">August</span>
    </div>
    <h2 class="post-title">Lorem ipsum dolor sit amet consectetuer</h2>
    <div class="post-meta"><span>Posted by Admin</span><span class="comments">5 Comments</span></div>
    <div class="post-image photo-group" role="img" aria-label="Group of players with rackets standing at the net"></div>
    <div class="post-excerpt">
      <p>Lorem ipsum dolor sit amet, consectetur adipiscing elit. Sed lacus mi, sollicitudin vehicula sapien ac, sodales eleifend nisl. Aenean vestibulum justo ac ultrices facilisis. Aliquam sit amet fringilla justo. Phasellus at suscipit mauris.</p>
      <p>Morbi eget diam nisi. Pellentesque dapibus faucibus neque. Cras pulvinar semper orci adipiscing commodo. Mauris ullamcorper arcu vel rutrum ultricies.</p>
    </div>
    <a class="read-more">Read more</a>
  </article>

  <article class="post" style="top:837px">
    <div class="post-date">
      <svg width="36" height="40" viewBox="0 0 36 40"><rect x="1" y="5" width="34" height="34" rx="3" fill="#fff" stroke="#cfcfcf" stroke-width="2"/><rect x="1" y="5" width="34" height="8" fill="#d4d4d4"/><rect x="8" y="1" width="3" height="8" rx="1" fill="#bdbdbd"/><rect x="25" y="1" width="3" height="8" rx="1" fill="#bdbdbd"/></svg>
      <span class="day">21</span><span class="month">July</span>
    </div>
    <h2 class="post-title">Lorem ipsum dolor sit amet consectetuer</h2>
    <div class="post-meta"><span>Posted by Admin</span><span class="comments">5 Comments</span></div>
    <div class="post-image photo-match" role="img" aria-label="Doubles players in pink striking a forehand during a match"></div>
    <div class="post-excerpt">
      <p>Lorem ipsum dolor sit amet, consectetur adipiscing elit. Sed lacus mi, sollicitudin vehicula sapien ac, sodales eleifend nisl. Aenean vestibulum justo ac ultrices facilisis. Aliquam sit amet fringilla justo. Phasellus at suscipit mauris.</p>
      <p>Morbi eget diam nisi. Pellentesque dapibus faucibus neque. Cras pulvinar semper orci adipiscing commodo. Mauris ullamcorper arcu vel rutrum ultricies.</p>
    </div>
    <a class="read-more">Read more</a>
  </article>

  <div class="pagination">
    <span class="current">1</span><span>2</span><span>3</span><span>4</span>
  </div>
</main>

<aside class="sidebar">
  <div class="search">
    <div class="button">
      <svg width="12" height="12" viewBox="0 0 12 12"><circle cx="5" cy="5" r="3.6" fill="none" stroke="#fff" stroke-width="1.5"/><line x1="7.6" y1="7.6" x2="11" y2="11" stroke="#fff" stroke-width="1.6"/></svg>
    </div>
    <div class="field">Search..</div>
  </div>

  <h3 class="widget-title" style="top:36px">Events</h3>
  <ul class="link-list" style="top:66px">
    <li><svg width="5" height="8" viewBox="0 0 5 8"><path d="M1 1l3 3-3 3" fill="none" stroke="#d8c600" stroke-width="1.4"/></svg>Event title</li>
    <li><svg width="5" height="8" viewBox="0 0 5 8"><path d="M1 1l3 3-3 3" fill="none" stroke="#d8c600" stroke-width="1.4"/></svg>Event title</li>
    <li><svg width="5" height="8" viewBox="0 0 5 8"><path d="M1 1l3 3-3 3" fill="none" stroke="#d8c600" stroke-width="1.4"/></svg>Event title</li>
    <li><svg width="5" height="8" viewBox="0 0 5 8"><path d="M1 1l3 3-3 3" fill="none" stroke="#d8c600" stroke-width="1.4"/></svg>Event title</li>
    <li><svg width="5" height="8" viewBox="0 0 5 8"><path d="M1 1l3 3-3 3" fill="none" stroke="#d8c600" stroke-width="1.4"/></svg>Event title</li>
    <li><svg width="5" height="8" viewBox="0 0 5 8"><path d="M1 1l3 3-3 3" fill="none" stroke="#d8c600" stroke-width="1.4"/></svg>Event title</li>
    <li><svg width="5" height="8" viewBox="0 0 5 8"><path d="M1 1l3 3-3 3" fill="none" stroke="#d8c600" stroke-width="1.4"/></svg>Event title</li>
    <li><svg width="5" height="8" viewBox="0 0 5 8"><path d="M1 1l3 3-3 3" fill="none" stroke="#d8c600" stroke-width="1.4"/></svg>Event title</li>
    <li><svg width="5" height="8" viewBox="0 0 5 8"><path d="M1 1l3 3-3 3" fill="none" stroke="#d8c600" stroke-width="1.4"/></svg>Event title</li>
  </ul>

  <h3 class="widget-title" style="top:232px">Archive</h3>
  <ul class="link-list" style="top:262px">
    <li><svg width="5" height="8" viewBox="0 0 5 8"><path d="M1 1l3 3-3 3" fill="none" stroke="#d8c600" stroke-width="1.4"/></svg>March 2014</li>
    <li><svg width="5" height="8" viewBox="0 0 5 8"><path d="M1 1l3 3-3 3" fill="none" stroke="#d8c600" stroke-width="1.4"/></svg>February 2014</li>
    <li><svg width="5" height="8" viewBox="0 0 5 8"><path d="M1 1l3 3-3 3" fill="none" stroke="#d8c600" stroke-width="1.4"/></svg>January 2014</li>
    <li><svg width="5" height="8" viewBox="0 0 5 8"><path d="M1 1l3 3-3 3" fill="none" stroke="#d8c600" stroke-width="1.4"/></svg>December 2013</li>
    <li><svg width="5" height="8" viewBox="0 0 5 8"><path d="M1 1l3 3-3 3" fill="none" stroke="#d8c600" stroke-width="1.4"/></svg>November 2013</li>
    <li><svg width="5" height="8" viewBox="0 0 5 8"><path d="M1 1l3 3-3 3" fill="none" stroke="#d8c600" stroke-width="1.4"/></svg>October 2013</li>
    <li><svg width="5" height="8" viewBox="0 0 5 8"><path d="M1 1l3 3-3 3" fill="none" stroke="#d8c600" stroke-width="1.4"/></svg>September 2013</li>
    <li><svg width="5" height="8" viewBox="0 0 5 8"><path d="M1 1l3 3-3 3" fill="none" stroke="#d8c600" stroke-width="1.4"/></svg>August 2013</li>
    <li><svg width="5" height="8" viewBox="0 0 5 8"><path d="M1 1l3 3-3 3" fill="none" stroke="#d8c600" stroke-width="1.4"/></svg>July 2013</li>
  </ul>

  <h3 class="widget-title" style="top:430px">Latest comments</h3>
  <ul class="comment-list">
    <li><span class="avatar"></span><div class="body"><div class="author">User #1 <em>says:</em></div><div class="quote">Contrary to popular belief..</div></div></li>
    <li><span class="avatar"></span><div class="body"><div class="author">User #2 <em>says:</em></div><div class="quote">Contrary to popular belief..</div></div></li>
    <li><span class="avatar"></span><div class="body"><div class="author">User #3 <em>says:</em></div><div class="quote">Contrary to popular belief..</div></div></li>
    <li><span class="avatar"></span><div class="body"><div class="author">User #4 <em>says:</em></div><div class="quote">Contrary to popular belief..</div></div></li>
    <li><span class="avatar"></span><div class="body"><div class="author">User #5 <em>says:</em></div><div class="quote">Contrary to popular belief..</div></div></li>
  </ul>
</aside>

<footer class="site-footer">
  <svg class="footer-icon" style="left:172px" width="10" height="14" viewBox="0 0 10 14"><path d="M5 0C2.2 0 0 2.2 0 5c0 3.6 5 9 5 9s5-5.4 5-9c0-2.8-2.2-5-5-5z" fill="#d8c600"/><circle cx="5" cy="5" r="2" fill="#363d45"/></svg>
  <div class="footer-block" style="left:197px">Courtside Heritage Trust<br>Street name<br>City name</div>

  <svg class="footer-icon" style="left:342px" width="9" height="14" viewBox="0 0 9 14"><rect x="0.5" y="0.5" width="8" height="13" rx="1.5" fill="none" stroke="#d8c600" stroke-width="1.4"/><rect x="2" y="2.5" width="5" height="7" fill="#d8c600"/></svg>
  <div class="footer-block" style="left:365px">Telephone: +1 800 555 0137<br>E-mail:<br>info@courtsidetrust.org</div>

  <div class="footer-legal"><span class="name">Courtside Heritage Trust</span> © 2014 | Privacy Policy</div>
  <div class="social"><span></span><span></span><span></span><span></span></div>
</footer>

</body>
</html>
```